弊社は健診に携わる医療機関様向けに、さまざまな周辺サービスのお手伝いをさせていただいております。その中で、最も営業に力を注いでいきたいサービスが、「コールセンター」となっております。
既に「コールセンター」のチラシを持っておりますが、より詳細な業務内容をアピールしたく、この度、作品を募集いたします。
A4サイズのaiデータでの納品をお願いいたします。

この度はご提案いただき、ありがとうございました。
両面を使い、サービスの内容を細かく、且つわかりやすくまとめていただきましたので、決定いたしました。

素敵なDMのご提案、誠にありがとうございました。
また機会がございましたら、宜しくお願いいたします。

```html
<!DOCTYPE html>
<html lang="ja">
<head>
<meta charset="utf-8">
<title>健康診断 コールセンターサービス</title>
<link rel="stylesheet" href="https://fonts.googleapis.com/css2?family=Noto+Sans+JP:wght@400;500;700;900&family=Noto+Serif+JP:wght@600;900&display=swap">
<style>
:root{
  --orange:#ee7f22;
  --orange-dark:#d96a10;
  --peach:#fdeede;
  --peach-line:#f6c89c;
  --ink:#3a3a3a;
  --muted:#6b6b6b;
  --paper:#ffffff;
  --stone-a:#e9e4dc;
  --stone-b:#cfc7bb;
}
*{box-sizing:border-box;margin:0;padding:0}
html,body{width:846px;height:1200px;overflow:hidden;background:var(--paper)}
body{font-family:"Noto Sans JP",sans-serif;color:var(--ink);position:relative}
.flyer{position:absolute;inset:0;width:846px;height:1200px;
  background:repeating-linear-gradient(135deg,#fff 0 14px,#fbf4ec 14px 16px)}
/* header */
.masthead{position:absolute;left:40px;top:22px;display:flex;align-items:flex-end;gap:18px}
.masthead__title{font-family:"Noto Serif JP",serif;font-weight:900;font-size:62px;color:var(--orange);letter-spacing:4px;line-height:1}
.masthead__sub{font-family:"Noto Serif JP",serif;font-weight:600;font-size:30px;color:var(--orange);letter-spacing:2px;padding-bottom:4px}
.masthead__rule{position:absolute;left:40px;right:40px;top:98px;height:3px;background:var(--orange)}
/* worries */
.worries__lead{position:absolute;top:112px;left:0;width:846px;text-align:center;font-size:18px;font-weight:700;letter-spacing:2px}
.worries{position:absolute;top:146px;left:40px;width:766px;display:flex;gap:20px}
.worry{flex:1;display:flex;gap:8px;align-items:flex-start}
.worry__bubble{flex:1.3;background:#fff;border:2px solid var(--peach-line);border-radius:8px;padding:10px 10px;font-size:11.5px;line-height:1.6;color:var(--ink);position:relative}
.worry__bubble em{color:var(--orange);font-style:normal;font-weight:700}
.worry__figure{flex:1;height:130px;border-radius:6px;background:linear-gradient(180deg,#f3f0ec,#e3ded7)}
/* band */
.band{position:absolute;top:300px;left:40px;width:766px;height:38px;background:var(--orange);color:#fff;font-size:20px;font-weight:900;letter-spacing:3px;text-align:center;line-height:38px}
/* features */
.features{position:absolute;top:350px;left:40px;width:766px;display:grid;grid-template-columns:repeat(3,1fr);gap:12px}
.feature{background:#fff;border:1.5px solid var(--peach-line);height:130px;padding:10px 12px}
.feature__head{display:flex;align-items:center;justify-content:space-between;gap:6px;border-bottom:1.5px dashed var(--peach-line);padding-bottom:5px;margin-bottom:8px}
.feature__title{font-size:11.5px;font-weight:700;color:var(--orange);white-space:nowrap}
.feature__no{font-size:11px;color:var(--muted)}
.feature__body{display:flex;gap:10px}
.feature__icon{flex:0 0 48px;height:48px}
.feature__text{font-size:10.5px;line-height:1.65;color:var(--ink)}
/* results */
.results{position:absolute;top:642px;left:0;width:846px;height:210px}
.results__bg{position:absolute;inset:0;background:linear-gradient(120deg,var(--stone-a),var(--stone-b) 70%,#bfb6a8)}
.results__title{position:absolute;left:40px;top:18px;font-family:"Noto Serif JP",serif;font-weight:900;font-size:50px;color:#3b3530;letter-spacing:3px}
.results__title b{font-size:66px;color:var(--orange-dark)}
.results__text{position:absolute;left:40px;top:112px;width:766px;font-size:13px;line-height:1.85;font-weight:500;color:#2f2a25}
/* flow */
.flow{position:absolute;top:868px;left:40px;width:430px;height:240px;background:var(--peach);padding:14px 16px}
.flow__title{font-size:14px;font-weight:700;color:var(--orange);margin-bottom:10px}
.flow__steps{display:flex;align-items:center;gap:6px}
.step{width:118px;text-align:center}
.step__box{height:118px;background:#fff;border:2px solid var(--peach-line);display:flex;align-items:center;justify-content:center}
.step__label{margin-top:8px;font-size:10.5px;font-weight:700;white-space:nowrap}
.step__arrow{width:20px;height:30px}
.flow__note{margin-top:10px;font-size:10.5px;color:var(--muted)}
.about{position:absolute;top:868px;left:492px;width:314px;font-size:11.5px;line-height:1.85;color:var(--ink)}
.about__name{color:var(--orange);font-weight:700}
/* footer */
.footer{position:absolute;left:0;top:1124px;width:846px;height:76px;background:#fff;border-top:3px solid var(--orange);display:flex;align-items:center;justify-content:space-between;padding:0 24px}
.brand{display:flex;align-items:center;gap:8px;white-space:nowrap}
.brand__mark{width:24px;height:24px;border-radius:50%;background:var(--orange);flex:0 0 24px}
.brand__text{font-size:10px;line-height:1.5;font-weight:700;color:var(--ink)}
.contact{display:flex;align-items:baseline;gap:6px;color:var(--orange);font-weight:900;font-size:20px;letter-spacing:0.5px;white-space:nowrap}
.contact small{font-size:11px;font-weight:700;color:var(--ink);letter-spacing:0}
.contact--web{font-size:12px;font-weight:700;color:var(--ink);letter-spacing:0}
</style>
</head>
<body>
<div class="flyer">
  <header class="masthead">
    <h1 class="masthead__title">健康診断</h1>
    <p class="masthead__sub">コールセンターサービス</p>
  </header>
  <div class="masthead__rule"></div>

  <p class="worries__lead">こんなお悩みはありませんか？</p>
  <section class="worries">
    <div class="worry">
      <p class="worry__bubble">受診予約の<em>電話対応</em>に追われ、本来の業務に集中できない。人員も足りていない…</p>
      <div class="worry__figure" role="img" aria-label="悩む医療事務スタッフのイラスト"></div>
    </div>
    <div class="worry">
      <p class="worry__bubble">繁忙期に電話がつながらず、<em>受診者からの苦情</em>が増えている。対応品質も不安…</p>
      <div class="worry__figure" role="img" aria-label="困った表情の受付担当者のイラスト"></div>
    </div>
    <div class="worry">
      <p class="worry__bubble">電話窓口の新設には<em>設備と人材</em>が必要で、費用と手間がかかりすぎる…</p>
      <div class="worry__figure" role="img" aria-label="考え込む管理者のイラスト"></div>
    </div>
  </section>

  <h2 class="band">弊社のサービスはここが違います。</h2>

  <section class="features">
    <article class="feature">
      <div class="feature__head"><h3 class="feature__title">マニュアル・トークスクリプトの作成</h3><span class="feature__no">01</span></div>
      <div class="feature__body">
        <svg class="feature__icon" viewBox="0 0 48 48"><circle cx="24" cy="24" r="23" fill="#fdeede"/><rect x="14" y="10" width="20" height="28" rx="2" fill="none" stroke="#ee7f22" stroke-width="2.5"/><path d="M18 18h12M18 24h12M18 30h8" stroke="#ee7f22" stroke-width="2.5"/></svg>
        <p class="feature__text">貴院の運用に合わせて専用のマニュアルを作成。対応品質を一定に保ちます。</p>
      </div>
    </article>
    <article class="feature">
      <div class="feature__head"><h3 class="feature__title">急な変更もすぐにチャットで共有</h3><span class="feature__no">02</span></div>
      <div class="feature__body">
        <svg class="feature__icon" viewBox="0 0 48 48"><circle cx="24" cy="24" r="23" fill="#fdeede"/><path d="M11 14h26v16H22l-7 6v-6h-4z" fill="none" stroke="#ee7f22" stroke-width="2.5" stroke-linejoin="round"/><circle cx="18" cy="22" r="1.8" fill="#ee7f22"/><circle cx="24" cy="22" r="1.8" fill="#ee7f22"/><circle cx="30" cy="22" r="1.8" fill="#ee7f22"/></svg>
        <p class="feature__text">枠の変更や休診などの連絡もチャットで即時に反映。柔軟に対応します。</p>
      </div>
    </article>
    <article class="feature">
      <div class="feature__head"><h3 class="feature__title">インフラ整備の負担軽減</h3><span class="feature__no">03</span></div>
      <div class="feature__body">
        <svg class="feature__icon" viewBox="0 0 48 48"><circle cx="24" cy="24" r="23" fill="#fdeede"/><path d="M16 12c2 0 4 5 4 7s-3 3-3 3c1 4 4 7 8 8 0 0 1-3 3-3s7 2 7 4-3 5-5 5c-9 0-18-9-18-18 0-2 2-6 4-6z" fill="none" stroke="#ee7f22" stroke-width="2.5" stroke-linejoin="round"/></svg>
        <p class="feature__text">回線や機器の準備は不要。設備投資をかけずにすぐ窓口を開設できます。</p>
      </div>
    </article>
    <article class="feature">
      <div class="feature__head"><h3 class="feature__title">メールや電話でも対応</h3><span class="feature__no">04</span></div>
      <div class="feature__body">
        <svg class="feature__icon" viewBox="0 0 48 48"><circle cx="24" cy="24" r="23" fill="#fdeede"/><rect x="11" y="15" width="26" height="18" rx="2" fill="none" stroke="#ee7f22" stroke-width="2.5"/><path d="M11 16l13 10 13-10" fill="none" stroke="#ee7f22" stroke-width="2.5"/></svg>
        <p class="feature__text">受診者からの問い合わせはメールや電話で受付。窓口を一本化できます。</p>
      </div>
    </article>
    <article class="feature">
      <div class="feature__head"><h3 class="feature__title">毎日、受電状況を確認できる</h3><span class="feature__no">05</span></div>
      <div class="feature__body">
        <svg class="feature__icon" viewBox="0 0 48 48"><circle cx="24" cy="24" r="23" fill="#fdeede"/><path d="M12 36h24" stroke="#ee7f22" stroke-width="2.5"/><rect x="14" y="24" width="5" height="10" fill="#ee7f22"/><rect x="22" y="18" width="5" height="16" fill="#ee7f22"/><rect x="30" y="12" width="5" height="22" fill="#ee7f22"/></svg>
        <p class="feature__text">受電件数や予約状況を日次で報告。現状をいつでも把握できます。</p>
      </div>
    </article>
    <article class="feature">
      <div class="feature__head"><h3 class="feature__title">繁忙期の人員調整も可能</h3><span class="feature__no">06</span></div>
      <div class="feature__body">
        <svg class="feature__icon" viewBox="0 0 48 48"><circle cx="24" cy="24" r="23" fill="#fdeede"/><path d="M14 24l7 7 13-14" fill="none" stroke="#ee7f22" stroke-width="3.5" stroke-linecap="round" stroke-linejoin="round"/></svg>
        <p class="feature__text">予約が集中する時期はオペレーターを増員。無駄なく効率的に運営します。</p>
      </div>
    </article>
  </section>

  <section class="results">
    <div class="results__bg" role="img" aria-label="落ち着いた色調の背景写真"></div>
    <h2 class="results__title"><b>20</b>万人以上の実績</h2>
    <p class="results__text">弊社の会員のヘルスラボ中央様、メディサポート東和様をはじめ、全国の健診機関様から多くのご依頼をいただいております。東京都、神奈川県、埼玉県、千葉県、静岡県、長野県など、各地の医療機関様の予約受付業務を担当しております。</p>
  </section>

  <section class="flow">
    <h3 class="flow__title">導入までの流れ</h3>
    <div class="flow__steps">
      <div class="step">
        <div class="step__box"><svg width="54" height="54" viewBox="0 0 48 48"><path d="M10 14h28v16H24l-8 6v-6h-6z" fill="none" stroke="#ee7f22" stroke-width="2.5" stroke-linejoin="round"/></svg></div>
        <p class="step__label">ヒアリング</p>
      </div>
      <svg class="step__arrow" viewBox="0 0 20 30"><path d="M4 4l12 11L4 26z" fill="#ee7f22"/></svg>
      <div class="step">
        <div class="step__box"><svg width="54" height="54" viewBox="0 0 48 48"><rect x="13" y="8" width="22" height="32" rx="2" fill="none" stroke="#ee7f22" stroke-width="2.5"/><path d="M18 16h12M18 22h12M18 28h8" stroke="#ee7f22" stroke-width="2.5"/></svg></div>
        <p class="step__label">トークスクリプト作成</p>
      </div>
      <svg class="step__arrow" viewBox="0 0 20 30"><path d="M4 4l12 11L4 26z" fill="#ee7f22"/></svg>
      <div class="step">
        <div class="step__box"><svg width="54" height="54" viewBox="0 0 48 48"><circle cx="24" cy="24" r="16" fill="none" stroke="#ee7f22" stroke-width="2.5"/><path d="M16 24l6 6 11-12" fill="none" stroke="#ee7f22" stroke-width="3" stroke-linecap="round" stroke-linejoin="round"/></svg></div>
        <p class="step__label">稼働開始</p>
      </div>
    </div>
    <p class="flow__note">最短2週間で稼働開始。詳しくはお問い合わせください。</p>
  </section>

  <p class="about"><span class="about__name">株式会社ミライケア総研</span>は健診機関様の周辺業務を幅広く支援しております。コールセンターサービスでは予約受付から変更・キャンセル対応、受診案内までを一括でお引き受けし、貴院のスタッフ様が本来の業務に専念できる環境をつくります。運用の細かなご要望にも柔軟にお応えいたしますので、まずはお気軽にご相談ください。</p>

  <footer class="footer">
    <div class="brand">
      <span class="brand__mark"></span>
      <p class="brand__text">お問い合わせ<br>株式会社ミライケア総研</p>
    </div>
    <p class="contact"><small>TEL</small>012-345-6780</p>
    <p class="contact"><small>FAX</small>012-345-6781</p>
    <p class="contact contact--web">https://www.miraicare-soken.jp/</p>
  </footer>
</div>
</body>
</html>
```